Halbrook Masonry- Business Card Design

We need a business card design for a new company based in Canberra ACT. We build Rock Retaining Walls, commercial and domestic.
We would like to see designs that use HM letters combine as logo and use stone sandstone or blue rocks. Final design of the business card should communicate strong, wealthy, Rock retaining walls

Target Market(s)

Everybody who needs stone retaining wall in there backyard

Industry/Entity Type

Business

Contact Information for Business Card

HM
Halbrook Masonry,
Dario Veltek (Stonemason)
Phone/ 0498 317 245
PO Box 3958 Kenley ACT 2609
E-mail/dveltek@tarnimail.net.au
www.halbrookmasonry.com.au

Requirements
Must have
• Letters HM combine as logo. "HALBROOK MASONRY" as features
Nice to have
• Rock: Sandstone or bluestone

```html
<!DOCTYPE html>
<html lang="en">
<head>
<meta charset="utf-8">
<title>Halbrook Masonry – Business Card</title>
<link href="https://fonts.googleapis.com/css2?family=Oswald:wght@500;600;700&family=Montserrat:wght@600;700&display=swap" rel="stylesheet">
<style>
  :root {
    --slate: #5f636c;
    --slate-light: #6b707a;
    --stone-pale: #eff0f4;
    --blue-stone: #9ea7c2;
    --blue-stone-dim: #7f879e;
    --white: #ffffff;
    --border: #8d9097;
    --label: #222222;
  }
  * { margin: 0; padding: 0; box-sizing: border-box; }
  html, body { width: 1200px; height: 1200px; overflow: hidden; background: var(--white); }
  .sheet { position: relative; width: 1200px; height: 1200px; }
  .side-label {
    position: absolute; left: 187px;
    font: 14px Arial, Helvetica, sans-serif; color: var(--label);
  }
  .side-label.front { top: 90px; }
  .side-label.back { top: 625px; }
  .card {
    position: absolute; left: 187px; width: 807px; height: 466px; overflow: hidden;
  }
  .card-front { top: 114px; border: 1px solid var(--border); background: var(--white); }
  .card-back { top: 650px; background: var(--slate); }

  .brand-mark {
    position: absolute; left: 350px; top: 84px; width: 106px; height: 106px;
    background: var(--slate); border-radius: 6px;
  }
  .brand-name {
    position: absolute; left: 0; right: 0; top: 252px; text-align: center;
    font-family: 'Oswald', sans-serif; font-weight: 600; font-size: 58px;
    letter-spacing: 1px; color: var(--slate); line-height: 1;
  }
  .stone-band {
    position: absolute; left: 0; right: 0; bottom: 0; height: 74px;
  }
  .card-front .stone-band { background: var(--stone-pale); }
  .card-back .stone-band { bottom: 26px; height: 52px; background: var(--slate-light); }

  .back-emblem {
    position: absolute; left: 322px; top: 40px; width: 170px; height: 170px;
    border-radius: 50%; background: var(--slate-light);
  }
  .person-name {
    position: absolute; left: 0; right: 0; top: 114px; text-align: center;
    font-family: 'Oswald', sans-serif; font-weight: 700; font-size: 52px;
    color: var(--white); line-height: 1;
  }
  .person-role {
    position: absolute; left: 0; right: 0; top: 176px; text-align: center;
    font-family: 'Montserrat', sans-serif; font-weight: 700; font-size: 14px;
    letter-spacing: 9px; color: var(--blue-stone-dim); padding-left: 9px;
  }
  .contact {
    position: absolute; left: 0; right: 0; text-align: center;
    font-family: 'Montserrat', sans-serif; font-weight: 700; color: var(--white);
    letter-spacing: 3px; line-height: 1;
  }
  .contact-row { top: 287px; font-size: 20px; }
  .contact-row .field + .field { margin-left: 28px; }
  .contact-label {
    font-family: 'Oswald', sans-serif; font-weight: 600; font-size: 15px;
    letter-spacing: 0.5px; color: var(--blue-stone); margin-right: 10px;
  }
  .address { top: 328px; font-size: 19px; }
  .website { top: 356px; font-size: 18px; }
</style>
</head>
<body>
<div class="sheet">
  <div class="side-label front">FRONT</div>
  <section class="card card-front">
    <div class="brand-mark"></div>
    <div class="brand-name">HALBROOK MASONRY</div>
    <div class="stone-band" role="img" aria-label="Pale dry-stone wall pattern along the bottom edge"></div>
  </section>

  <div class="side-label back">BACK</div>
  <section class="card card-back">
    <div class="back-emblem"></div>
    <div class="person-name">DARIO VELTEK</div>
    <div class="person-role">STONEMASON</div>
    <div class="contact contact-row">
      <span class="field"><span class="contact-label">PHONE:</span>0498 317 245</span>
      <span class="field"><span class="contact-label">EMAIL:</span>dveltek@tarnimail.net.au</span>
    </div>
    <div class="contact address">PO Box 3958 Kenley ACT 2609</div>
    <div class="contact website">www.halbrookmasonry.com.au</div>
    <div class="stone-band" role="img" aria-label="Muted grey dry-stone wall pattern along the bottom"></div>
  </section>
</div>
</body>
</html>
```